Design a corporate looking website for Harbourline Funding

Need design only WordPress mock up for Harbourline Funding who provides short term finance solutions to other businesses. We need a corporate looking website that depicts a trustworthy, Dynamic fast acting company.
Visit http://q7.pagemockery.net/ for current mock up We need something like e this but not the same with a design that depicts corporate with more colour and images, needs to install trust and fast action. Please feel free to change the layout as I am not wedded to current design but am happy with what on the landing page.

Target Market(s)

Small to medium sized Businesses

Industry/Entity Type

Finance

Number of Pages Required

1 page

Font styles to use
Sans Serif

Requirements
Must have
• Design Landing pages in WordPress
• Visit http://q7.pagemockery.net/ for current mock up need Layout like this but with a design that depicts corporate with more colour and images, needs to install trust and fast action. Please feel free to change the layout as I am not happy with current design but am wedded to what on the landing page.
Should not have
• any copyright material on it.

```html
<!DOCTYPE html>
<html lang="en">
<head>
<meta charset="utf-8">
<title>Harbourline Funding</title>
<link rel="stylesheet" href="https://fonts.googleapis.com/css2?family=Source+Sans+3:wght@300;400;600;700&display=swap">
<style>
:root{
  --blue:#56a0f8;
  --blue-dark:#2f7fe0;
  --navy:#1b3a6b;
  --orange:#fb7a1e;
  --violet:#a63fd6;
  --indigo:#5a74f4;
  --text:#4a4a4a;
  --muted:#7a7a7a;
  --footer:#3a3b3d;
  --footer-bar:#2b2c2e;
  --line:#55575a;
  --white:#ffffff;
}
*{box-sizing:border-box;margin:0;padding:0}
html,body{width:1200px;height:2542px;overflow:hidden}
body{font-family:"Source Sans 3",Arial,sans-serif;color:var(--text);background:var(--white);position:relative}
.abs{position:absolute}

/* header */
.site-header{left:0;top:0;width:1200px;height:112px;background:var(--white)}
.brand{left:47px;top:34px;display:flex;align-items:center;gap:12px}
.brand-dot{width:34px;height:34px;border-radius:50%;background:var(--blue-dark)}
.brand-name{font-size:28px;font-weight:700;color:var(--navy);letter-spacing:.5px}
.main-nav{right:45px;top:42px;display:flex;gap:22px;font-size:18px;font-weight:600;color:#222}
.main-nav .active{color:var(--navy);border-bottom:3px solid var(--navy);padding-bottom:6px}

/* hero */
.hero{left:0;top:112px;width:1200px;height:637px;background:linear-gradient(90deg,var(--violet) 0%,#8a55e6 45%,var(--indigo) 100%)}
.hero-photo{left:0;top:0;width:1200px;height:637px;background:radial-gradient(ellipse at 30% 45%,rgba(255,220,230,.28),rgba(255,255,255,0) 60%)}
.hero-title{left:212px;top:196px;font-size:37px;font-weight:700;color:var(--white)}
.hero-text{left:212px;top:240px;width:400px;font-size:17px;line-height:25px;color:var(--white)}
.contact-card{left:697px;top:122px;width:315px;height:393px;background:var(--white);box-shadow:0 2px 8px rgba(0,0,0,.2)}
.contact-card h3{position:absolute;left:22px;top:14px;font-size:24px;font-weight:600;color:#555}
.field{position:absolute;left:22px;width:271px;height:37px;border:1.5px solid #666;border-radius:3px;font-size:10px;color:#666;padding:10px 14px;letter-spacing:.3px}
.field svg{position:absolute;right:12px;top:11px}
.field.msg{height:88px}
.submit{position:absolute;left:22px;top:332px;width:271px;height:38px;background:var(--blue);color:var(--white);font-size:16px;font-weight:600;text-align:center;line-height:38px;letter-spacing:.5px}

/* services */
.section-title{left:0;width:1200px;text-align:center;font-size:36px;font-weight:300;color:#444}
.service{width:220px;text-align:center;font-size:17px;line-height:22px;color:#555}
.service svg{display:block;margin:0 auto 6px}
.more{display:inline-block;margin-top:3px;width:83px;height:26px;line-height:26px;border-radius:4px;background:var(--blue);color:var(--white);font-size:14px}
.service.hot .more{background:var(--orange)}

/* parallax band */
.band{left:0;top:1258px;width:1200px;height:242px;background:linear-gradient(90deg,var(--violet) 0%,#8a55e6 45%,var(--indigo) 100%)}
.band-text{left:0;top:76px;width:1200px;text-align:center;font-size:33px;font-weight:400;color:var(--white)}
.band-btn{left:509px;top:139px;width:182px;height:38px;background:var(--orange);color:var(--white);font-size:21px;text-align:center;line-height:38px;border-radius:5px}

/* why us */
.sub-title{font-size:25px;font-weight:400;color:#444}
.video{left:47px;top:1659px;width:397px;height:236px;background:linear-gradient(135deg,#3a3f55,#8b4a4a 45%,#c9793c 70%,#2b2d3a)}
.play{left:220px;top:1760px;width:50px;height:34px;background:rgba(0,0,0,.7);border-radius:4px}
.why-text{left:490px;top:1652px;width:663px;font-size:15px;line-height:25px;color:#555}
.pill{height:38px;line-height:38px;border-radius:5px;color:var(--white);font-size:21px;text-align:center}
.pill.blue{left:491px;top:1858px;width:307px;background:var(--blue)}
.pill.orange{left:818px;top:1858px;width:284px;background:var(--orange)}

/* testimonials */
.testimonials{left:0;top:2009px;width:1200px;height:242px;background:var(--blue)}
.testimonials h2{position:absolute;left:0;top:36px;width:1200px;text-align:center;font-size:35px;font-weight:400;color:var(--white)}
.quote{position:absolute;left:300px;top:106px;width:600px;text-align:center;font-size:16px;line-height:25px;color:var(--white)}
.quote-by{position:absolute;left:0;top:164px;width:1200px;text-align:center;font-size:11px;color:#233;font-weight:700}
.quote-by em{font-weight:400}

/* footer */
.site-footer{left:0;top:2251px;width:1200px;height:241px;background:var(--footer)}
.foot-col{position:absolute;top:38px;width:225px;font-size:11px;color:#ddd}
.foot-col h4{font-size:11px;font-weight:600;letter-spacing:.3px;margin-bottom:17px}
.foot-col li{list-style:none;padding:0 0 11px;margin-bottom:11px;border-bottom:1px solid var(--line)}
.foot-bar{left:0;top:2492px;width:1200px;height:50px;background:var(--footer-bar)}
.copy{position:absolute;left:111px;top:18px;font-size:11px;color:#999}
.copy b{color:#ddd;font-weight:400}
.social{position:absolute;left:950px;top:17px;display:flex;gap:16px}
.social span{width:14px;height:14px;border-radius:50%;background:var(--orange)}
.to-top{position:absolute;left:1131px;top:22px;width:44px;height:28px;background:#444649;border-radius:3px 3px 0 0}
</style>
</head>
<body>

<header class="site-header abs">
  <div class="brand abs"><span class="brand-dot"></span><span class="brand-name">HARBOURLINE FUNDING</span></div>
  <nav class="main-nav abs">
    <span class="active">Home</span><span>Services</span><span>Why Commisions</span><span>Investors</span><span>About Us</span><span>Contact Us</span><span>Members Login</span>
  </nav>
</header>

<section class="hero abs">
  <div class="hero-photo abs" role="img" aria-label="Smiling family of three embracing, tinted purple-blue"></div>
  <h1 class="hero-title abs">YOUR TITLE HERE</h1>
  <p class="hero-text abs">Cetero utroque nusquam ad qui, ea mea quas menandri. Te rebum offendit consetetur sed, nobis interesset sed ne. Quando vulputate ex ius. Facer accusata splendide in nam, erat commune id quo. Et porro deserunt persequeris nam, ei stet congue interesset mea. Pro ad consulatu conceptam.</p>
  <form class="contact-card abs">
    <h3>CONTACT US</h3>
    <div class="field" style="top:56px">NAME<svg width="16" height="14" viewBox="0 0 16 14"><path d="M2 7l4 4 8-9" fill="none" stroke="#3a9a3a" stroke-width="2.2"/></svg></div>
    <div class="field" style="top:113px">EMAIL<svg width="12" height="12" viewBox="0 0 12 12"><path d="M2 2l8 8M10 2l-8 8" stroke="#e03a3a" stroke-width="1.8"/></svg></div>
    <div class="field" style="top:173px">PHONE NUMBER</div>
    <div class="field msg" style="top:229px">MESSAGE</div>
    <div class="submit">SUBMIT</div>
  </form>
</section>

<h2 class="section-title abs" style="top:782px">WHAT WE CAN DO FOR YOU!</h2>

<div class="service abs" style="left:129px;top:884px"><svg width="66" height="56" viewBox="0 0 66 56"><path d="M33 2L2 30h9v24h16V38h12v16h16V30h9L52 19V6h-8v6z" fill="#56a0f8"/></svg>RESINDENTIAL REAL<br>ESTATE AGENTS<br><span class="more">MORE</span></div>
<div class="service abs" style="left:370px;top:884px"><svg width="66" height="56" viewBox="0 0 66 56"><path d="M33 2L2 30h9v24h16V38h12v16h16V30h9L52 19V6h-8v6z" fill="#56a0f8"/></svg>RESINDENTIAL REAL<br>ESTATE AGENTS<br><span class="more">MORE</span></div>
<div class="service hot abs" style="left:610px;top:884px"><svg width="66" height="56" viewBox="0 0 66 56"><path d="M33 2L2 30h9v24h16V38h12v16h16V30h9L52 19V6h-8v6z" fill="#fb7a1e"/></svg>RESINDENTIAL REAL<br>ESTATE AGENTS<br><span class="more">MORE</span></div>
<div class="service abs" style="left:851px;top:884px"><svg width="66" height="56" viewBox="0 0 66 56"><path d="M33 2L2 30h9v24h16V38h12v16h16V30h9L52 19V6h-8v6z" fill="#56a0f8"/></svg>RESINDENTIAL REAL<br>ESTATE AGENTS<br><span class="more">MORE</span></div>
<div class="service abs" style="left:129px;top:1073px"><svg width="66" height="56" viewBox="0 0 66 56"><path d="M33 2L2 30h9v24h16V38h12v16h16V30h9L52 19V6h-8v6z" fill="#56a0f8"/></svg>RESINDENTIAL REAL<br>ESTATE AGENTS<br><span class="more">MORE</span></div>
<div class="service abs" style="left:370px;top:1073px"><svg width="66" height="56" viewBox="0 0 66 56"><path d="M33 2L2 30h9v24h16V38h12v16h16V30h9L52 19V6h-8v6z" fill="#56a0f8"/></svg>RESINDENTIAL REAL<br>ESTATE AGENTS<br><span class="more">MORE</span></div>
<div class="service abs" style="left:610px;top:1073px"><svg width="66" height="56" viewBox="0 0 66 56"><path d="M33 2L2 30h9v24h16V38h12v16h16V30h9L52 19V6h-8v6z" fill="#56a0f8"/></svg>RESINDENTIAL REAL<br>ESTATE AGENTS<br><span class="more">MORE</span></div>
<div class="service abs" style="left:851px;top:1073px"><svg width="66" height="56" viewBox="0 0 66 56"><path d="M33 2L2 30h9v24h16V38h12v16h16V30h9L52 19V6h-8v6z" fill="#56a0f8"/></svg>RESINDENTIAL REAL<br>ESTATE AGENTS<br><span class="more">MORE</span></div>

<section class="band abs" role="img" aria-label="Family photo background with parallax, tinted purple-blue">
  <p class="band-text abs">SOME TEXT! THIS HAS PARALLAX EFFECT.</p>
  <div class="band-btn abs">CONTACT US</div>
</section>

<h2 class="section-title abs" style="top:1534px">WHY WITH US!</h2>
<h3 class="sub-title abs" style="left:128px;top:1606px">ABOUT OUR BUSINESS</h3>
<h3 class="sub-title abs" style="left:490px;top:1606px">WHY HARBOURLINE FUNDING</h3>
<div class="video abs" role="img" aria-label="Video thumbnail of a busy city square with billboards"></div>
<div class="play abs"><svg width="50" height="34" viewBox="0 0 50 34"><path d="M20 10l12 7-12 7z" fill="#fff"/></svg></div>
<p class="why-text abs">At Harbourline Funding our aim is to provide immediate commission advance solutions for all industries. Our background is sales, property and finance and we understand the issues faced with Small to medium Businesses, Agents, contractors and consultants who earn commissions. Unforeseen expenses, inconstant sales, holiday periods, sickness, taxation bills and job changes can all have an effect on a sales and commission flow.<br>Harbourline Funding are here to help if you have outstanding commissions that could be used now then we may have an answer, once approved you will have an advance on your outstanding commission within 4 hours.</p>
<div class="pill blue abs">OUR PRICING GUARANTEE</div>
<div class="pill orange abs">OUR LOYALTY PRAGRAM</div>

<section class="testimonials abs">
  <h2>WHAT PEOPLE SAY ABOUT US</h2>
  <svg class="abs" style="left:174px;top:120px" width="30" height="50" viewBox="0 0 30 50"><path d="M26 3L5 25l21 22" fill="none" stroke="#fff" stroke-width="4"/></svg>
  <svg class="abs" style="left:996px;top:120px" width="30" height="50" viewBox="0 0 30 50"><path d="M4 3l21 22L4 47" fill="none" stroke="#333" stroke-width="4"/></svg>
  <p class="quote">Great services. Very professional. Of course, this is just a placeholder testimonial, it will have to be replaced.</p>
  <p class="quote-by">MILO TRENT, <em>TRENT LOGISTICS</em></p>
</section>

<footer class="site-footer abs">
  <div class="foot-col" style="left:111px"><h4>ABOUT US</h4><ul><li>Home</li><li>Services</li><li>Why Commission</li></ul></div>
  <div class="foot-col" style="left:363px"><h4>HARBOURLINE FUNDING</h4><ul><li>Investors</li><li>Consultants</li><li>Testimonials</li></ul></div>
  <div class="foot-col" style="left:614px"><h4>MEMBERS LOGIN</h4><ul><li>Client Login</li><li>Consultant Login</li><li>Investor Login</li></ul></div>
  <div class="foot-col" style="left:866px"><h4>CONTACT DETAILS</h4><ul><li>12 Quayside Lane</li><li>Eastport 4021</li><li>Tel: 0400 555 218</li></ul></div>
</footer>
<div class="foot-bar abs">
  <p class="copy">Copyright © 2015 <b>Harbourline Funding</b>. All rights reserved.</p>
  <div class="social"><span></span><span></span><span></span><span></span><span></span></div>
  <div class="to-top"><svg width="44" height="28" viewBox="0 0 44 28"><path d="M17 17l5-5 5 5" fill="none" stroke="#ddd" stroke-width="2"/></svg></div>
</div>

</body>
</html>
```